Roles On Ledger - Job Board for Big Data Professionals

Hi all,

I need a design for a job board I'm kicking off that is focused on finding jobs and people that work in Data Analytics.

I've attached a fairly in depth design spec and wireframe giving a rough mockup. Please note that in the wireframe, the boxes are there to demonstrate orders of content. This is not to say that a lot of distinct content boxes will necessarily be the best way of presenting content.

I will be available on Chatterly (marcus.holloway) and email (h0ll0w4y@quillpost.net) and will give constant and clear feedback on the way.

Payment is not guaranteed yet. As soon as there are at least 5+ promising designs I will make this guaranteed.

Thanks
Marcus
Updates

Hi all

Please suspend all work on this project for the time being.

I am working closely with 1 designer who I will very likely accept their design.

I appreciate all the work you have put into this, but dont want to waste any more of your time.

Thanks
Marcus

Industry/Entity Type

Work

Requirements
Must have
• I'd like a clean, modern web design which has strong use of Typography. Strong use of a clear and consistent palette of colours.
Should not have
• Boxes with rounded edges

```html
<!DOCTYPE html>
<html lang="en">
<head>
<meta charset="utf-8">
<title>Roles On Ledger – Job Board</title>
<link href="https://fonts.googleapis.com/css2?family=Gelasio:ital,wght@0,400;0,600;1,400&family=Arimo:wght@400;700&display=swap" rel="stylesheet">
<style>
  :root {
    --page-blue: #0b69ae;
    --accent: #2d9fdc;
    --accent-dark: #1a83c0;
    --link: #1670b8;
    --ink: #222;
    --muted: #9a9a9a;
    --rule: #e3e3e3;
    --band: #ececec;
    --nav: #000;
    --subnav: #555;
    --nav-active: #4a4a4a;
    --row-alt: #efefef;
    --thumb: #666;
    --orange-1: #f7a823;
    --orange-2: #ee8a10;
    --white: #fff;
  }
  * { box-sizing: border-box; margin: 0; padding: 0; }
  html, body { width: 1098px; height: 1200px; overflow: hidden; }
  body { background: var(--page-blue); font-family: "Arimo", Arial, sans-serif; font-size: 11px; color: var(--ink); position: relative; }
  .serif { font-family: "Gelasio", Georgia, serif; }
  .page { position: absolute; left: 110px; top: 16px; width: 878px; height: 1006px; background: var(--white); }
  .abs { position: absolute; }

  /* header */
  .brand { left: 8px; top: 8px; font-family: "Gelasio", Georgia, serif; font-weight: 600; font-size: 28px; color: #111; letter-spacing: -0.3px; }
  .tagline { left: 9px; top: 40px; font-family: "Gelasio", Georgia, serif; font-style: italic; font-size: 12px; color: #555; }
  .account-links { right: 8px; top: 13px; font-family: "Gelasio", Georgia, serif; font-style: italic; font-size: 14px; color: #222; }
  .account-links span { margin: 0 6px; }
  .lang { right: 11px; top: 38px; width: 126px; height: 20px; border: 1px solid #bbb; font-family: "Gelasio", Georgia, serif; font-size: 12px; padding: 2px 6px; }
  .lang .arrow { position: absolute; right: 1px; top: 1px; width: 15px; height: 16px; border-left: 1px solid #bbb; }

  /* nav */
  .main-nav { left: 0; top: 72px; width: 878px; height: 30px; background: var(--nav); display: flex; padding-left: 8px; }
  .main-nav a { color: var(--white); text-decoration: none; font-family: "Gelasio", Georgia, serif; font-size: 15px; line-height: 30px; padding: 0 14px; }
  .main-nav a.active { background: var(--nav-active); }
  .sub-nav { left: 0; top: 102px; width: 878px; height: 31px; background: var(--subnav); display: flex; padding-left: 8px; }
  .sub-nav a { color: var(--white); text-decoration: none; font-family: "Gelasio", Georgia, serif; font-size: 14px; line-height: 31px; padding: 0 10px; margin-right: 6px; }
  .site-search { right: 9px; top: 7px; width: 106px; height: 19px; background: var(--white); border-radius: 10px; }
  .site-search svg { position: absolute; right: 8px; top: 4px; }

  /* section headings */
  .sec-head { display: flex; align-items: center; gap: 8px; font-family: "Gelasio", Georgia, serif; font-style: italic; font-size: 13px; color: #222; }
  .sec-head::after { content: ""; flex: 1; height: 9px; background: var(--band); }
  .band { height: 9px; background: var(--band); }

  .field { height: 20px; border: 1px solid #aaa; font-style: italic; font-size: 11px; color: #333; padding: 3px 7px; }
  .btn { background: var(--accent); color: var(--white); font-size: 11px; text-align: center; border: 1px solid var(--accent-dark); }

  /* boxes */
  .box { border: 1px solid #222; }
  .box-head { height: 30px; background: var(--accent); display: flex; justify-content: space-between; align-items: center; padding: 0 16px 0 18px; color: #123; }
  .box-head .title { font-family: "Gelasio", Georgia, serif; font-style: italic; font-size: 12px; color: #153a5a; }
  .box-head .more { font-family: "Gelasio", Georgia, serif; font-size: 12px; color: var(--white); display: flex; align-items: center; gap: 10px; }
  .plus { width: 11px; height: 11px; background: var(--white); position: relative; }
  .plus::before, .plus::after { content: ""; position: absolute; background: #555; }
  .plus::before { left: 2px; top: 5px; width: 7px; height: 1px; }
  .plus::after { left: 5px; top: 2px; width: 1px; height: 7px; }
  .cats { display: grid; grid-template-columns: 171px 1fr; padding: 13px 0 0 17px; row-gap: 0; }
  .cats div { line-height: 16.3px; font-size: 10.5px; }
  .job { height: 38.6px; padding: 5px 17px; font-size: 10.5px; line-height: 15px; }
  .job:nth-child(even) { background: var(--row-alt); }
  .job a { color: var(--link); text-decoration: none; }

  /* news */
  .news-item { display: flex; gap: 14px; height: 77px; border-bottom: 1px solid var(--rule); padding-top: 10px; }
  .thumb { width: 42px; height: 42px; background: var(--thumb); border: 2px solid #ddd; outline: 1px solid #bbb; flex: none; }
  .news-item .t { font-size: 10.5px; line-height: 17px; }
  .news-item .meta { font-family: "Gelasio", Georgia, serif; font-style: italic; font-size: 10px; color: #b5b5b5; }

  /* right column */
  .upload { background: linear-gradient(#fab33a, var(--orange-2)); }
  .tweet { border-bottom: 1px solid var(--rule); height: 74.5px; padding-top: 7px; font-size: 10.5px; line-height: 17px; }
  .tweet a { color: var(--link); text-decoration: none; }
  .tweet .ago { font-family: "Gelasio", Georgia, serif; font-style: italic; font-size: 9px; color: #999; line-height: 14px; }

  /* footer */
  .footer { position: absolute; left: 110px; top: 1022px; width: 878px; height: 159px; background: #000; color: var(--white); font-family: "Gelasio", Georgia, serif; font-size: 12px; }
  .footer ul { list-style: none; position: absolute; top: 21px; line-height: 15.4px; }
  .footer .brand-foot { position: absolute; right: 34px; top: 32px; font-size: 26px; font-weight: 600; }
  .footer .legal { position: absolute; right: 34px; top: 70px; text-align: right; font-size: 11.5px; line-height: 16px; }
</style>
</head>
<body>
<div class="page">
  <div class="abs brand">Roles On Ledger</div>
  <div class="abs tagline">the easy way to find perfect jobs</div>
  <div class="abs account-links">login<span>|</span>register</div>
  <div class="abs lang">English
    <div class="arrow"><svg width="15" height="16"><path d="M4 6h7l-3.5 4z" fill="#333"/></svg></div>
  </div>

  <nav class="abs main-nav">
    <a>Home</a><a class="active">Jobs</a><a>Account</a><a>Register</a><a>News &amp; Insight</a><a>Graduates</a><a>Recruiters</a><a>About</a>
  </nav>
  <nav class="abs sub-nav">
    <a>Advanced Job Search</a><a>Companies</a>
    <div class="abs site-search"><svg width="11" height="11"><circle cx="4.5" cy="4.5" r="3.2" fill="none" stroke="#999" stroke-width="1.4"/><path d="M7 7l3 3" stroke="#999" stroke-width="1.6"/></svg></div>
  </nav>

  <!-- left column -->
  <section class="abs" style="left:8px;top:156px;width:372px">
    <h2 class="sec-head">User Login</h2>
  </section>
  <div class="abs field" style="left:8px;top:185px;width:154px">username</div>
  <div class="abs field" style="left:171px;top:185px;width:155px">password</div>
  <div class="abs btn" style="left:334px;top:185px;width:33px;height:20px;line-height:18px">GO</div>
  <div class="abs" style="left:8px;top:215px;font-size:10px">Forgot Your Password? &nbsp;&nbsp;|&nbsp;&nbsp; Register</div>
  <div class="abs band" style="left:8px;top:244px;width:372px"></div>

  <section class="abs" style="left:8px;top:280px;width:372px">
    <h2 class="sec-head">Quick Search</h2>
  </section>
  <div class="abs field" style="left:8px;top:309px;width:178px">keyword</div>
  <div class="abs field" style="left:195px;top:309px;width:179px">location</div>
  <div class="abs" style="left:8px;top:340px;font-size:10.5px;display:flex;align-items:center;gap:10px">
    <b>Type</b>
    <span style="display:flex;align-items:center;gap:6px"><i style="width:11px;height:11px;border:1px solid #999;display:inline-block"></i>contract</span>
    <span style="display:flex;align-items:center;gap:6px;margin-left:8px"><i style="width:11px;height:11px;border:1px solid #999;display:inline-block"></i>permanent</span>
  </div>
  <div class="abs btn" style="left:8px;top:365px;width:59px;height:20px;line-height:18px;border-radius:3px">SEARCH</div>
  <div class="abs" style="left:277px;top:367px;font-size:10.5px;font-weight:700;color:#333;display:flex;align-items:center;gap:6px">advanced search
    <svg width="14" height="14"><rect width="14" height="14" fill="#2d9fdc"/><path d="M5 4l4 3-4 3z" fill="#fff"/></svg>
  </div>
  <div class="abs band" style="left:8px;top:402px;width:372px"></div>

  <section class="abs box" style="left:8px;top:438px;width:372px;height:166px">
    <div class="box-head"><span class="title">Job Categories</span><span class="more">see more <i class="plus"></i></span></div>
    <div class="cats">
      <div>Accountant (2)</div><div>Computer Engineering (2)</div>
      <div>Web Designer (10)</div><div>Web Designer (10)</div>
      <div>Programmer (8)</div><div>Programmer (8)</div>
      <div>Finance (15)</div><div>Finance (15)</div>
      <div>Consultant (3)</div><div>Consultant (3)</div>
      <div>Infomation Technology (2)</div><div>Lawyer (2)</div>
      <div>Banking (5)</div><div>Banking (5)</div>
    </div>
  </section>

  <section class="abs box" style="left:8px;top:628px;width:372px;height:344px">
    <div class="box-head"><span class="title">Featured Jobs</span><span class="more">see more <i class="plus"></i></span></div>
    <div>
      <div class="job"><a>Senior Interior Designer</a> in Tester Ltd<br>Fort, Lauderde, Florida</div>
      <div class="job"><a>Senior Interior Designer</a> in Tester Ltd<br>Fort, Lauderde, Florida</div>
      <div class="job"><a>Senior Interior Designer</a> in Tester Ltd<br>Fort, Lauderde, Florida</div>
      <div class="job"><a>Senior Interior Designer</a> in Tester Ltd<br>Fort, Lauderde, Florida</div>
      <div class="job"><a>Senior Interior Designer</a> in Tester Ltd<br>Fort, Lauderde, Florida</div>
      <div class="job"><a>Senior Interior Designer</a> in Tester Ltd<br>Fort, Lauderde, Florida</div>
      <div class="job"><a>Senior Interior Designer</a> in Tester Ltd<br>Fort, Lauderde, Florida</div>
      <div class="job"><a>Senior Interior Designer</a> in Tester Ltd<br>Fort, Lauderde, Florida</div>
    </div>
  </section>

  <!-- middle column -->
  <section class="abs" style="left:398px;top:156px;width:258px">
    <h2 class="sec-head">Latest News &amp; Insight</h2>
    <div style="margin-top:2px">
      <article class="news-item"><div class="thumb"></div><div><p class="t">Fly Fishers Serving as Transports for<br>Noxious Little Invaders</p><p class="meta">August 4 2010, 8 Comments</p></div></article>
      <article class="news-item"><div class="thumb"></div><div><p class="t">Fly Fishers Serving as Transports for<br>Noxious Little Invaders</p><p class="meta">August 4 2010, 8 Comments</p></div></article>
      <article class="news-item"><div class="thumb"></div><div><p class="t">Fly Fishers Serving as Transports for<br>Noxious Little Invaders</p><p class="meta">August 4 2010, 8 Comments</p></div></article>
      <article class="news-item"><div class="thumb"></div><div><p class="t">Fly Fishers Serving as Transports for<br>Noxious Little Invaders</p><p class="meta">August 4 2010, 8 Comments</p></div></article>
      <article class="news-item"><div class="thumb"></div><div><p class="t">Fly Fishers Serving as Transports for<br>Noxious Little Invaders</p><p class="meta">August 4 2010, 8 Comments</p></div></article>
    </div>
  </section>
  <section class="abs" style="left:398px;top:580px;width:258px">
    <h2 class="sec-head">Email Job Alerts</h2>
  </section>
  <div class="abs field" style="left:398px;top:610px;width:176px;font-style:normal">e-mail</div>
  <div class="abs btn" style="left:582px;top:610px;width:76px;height:20px;line-height:18px;font-weight:700">SUBSCRIBE</div>
  <div class="abs" style="left:398px;top:646px;width:258px;border-top:1px solid var(--rule)"></div>
  <section class="abs" style="left:398px;top:668px;width:258px">
    <h2 class="sec-head">Advertisement</h2>
  </section>
  <div class="abs" style="left:399px;top:699px;width:257px;height:214px;border:1px solid #ccc;display:flex;align-items:center;justify-content:center;font-size:10px;color:#555">300 x 250</div>

  <!-- right column -->
  <div class="abs upload" style="left:673px;top:151px;width:199px;height:95px">
    <div class="abs serif" style="left:28px;top:10px;font-size:21px;font-weight:600;color:#fff">Upload Resume</div>
    <div class="abs" style="left:30px;top:40px;font-size:9.5px;font-weight:700;color:#fff">show your resume to job seeker</div>
    <div class="abs" role="img" aria-label="Illustration of a globe with a mouse cursor" style="left:6px;top:55px;width:60px;height:36px;border-radius:50%;background:radial-gradient(#fff,#c9c9c9 60%,#8a8a8a)"></div>
    <div class="abs" style="left:96px;top:61px;width:96px;height:17px;background:#f49a18;border:1px solid #fbd08a;font-size:9px;color:#fff;line-height:15px;padding-left:8px">&#10140; UPLOAD NOW</div>
  </div>
  <section class="abs" style="left:673px;top:270px;width:199px">
    <h2 class="sec-head">Social Feed</h2>
    <div style="margin-top:6px">
      <div class="tweet">Lorem ipsum dul amet <a>http://qk.ln/ibXdjY</a><br><a>#quillwp</a> #hashtag<p class="ago">31 minutes ago</p></div>
      <div class="tweet">Lorem ipsum dul amet <a>http://qk.ln/ibXdjY</a><br><a>#quillwp</a> #hashtag<p class="ago">31 minutes ago</p></div>
      <div class="tweet">Lorem ipsum dul amet <a>http://qk.ln/ibXdjY</a><br><a>#quillwp</a> #hashtag<p class="ago">31 minutes ago</p></div>
      <div class="tweet">Lorem ipsum dul amet <a>http://qk.ln/ibXdjY</a><br><a>#quillwp</a> #hashtag<p class="ago">31 minutes ago</p></div>
    </div>
  </section>
</div>

<footer class="footer">
  <ul style="left:34px"><li>Home</li><li>Jobs</li><li>Account</li><li>Register</li><li>News &amp; Insight</li><li>Graduates</li><li>Recruiters</li><li>About</li></ul>
  <ul style="left:155px"><li>Advanced Job Search</li><li>Companies</li></ul>
  <ul style="left:300px"><li>Login</li><li>Post Resume</li><li>Alerts</li><li>Settings</li></ul>
  <ul style="left:398px"><li>Login</li><li>Search Resumes</li><li>Advertising &amp; Branding Solutions</li></ul>
  <div class="brand-foot">Roles On Ledger</div>
  <div class="legal">Copyrights (c) Roles On Ledger 2011<br>Allrights reserved</div>
</footer>
</body>
</html>
```